Honey apple cider vinegar label

organic food company need a contemporary honey apple cider vinegar and honey vinegar label, natural GMP logo HACCP LOgo
label detail height :140mm Width:80mm
ingredient: honey, apple cider vinegar and water, free from artificial color & preservative
Shelf Life: 3 years
Net weight 400ml
Storage : store in cool place , do not expose to sunlight
instruction for use: add 20ml to a full glass of water 3, times a days before meal, stop consuming if allergies happen
certification, GMP HACCP, Halal, natural product

Target Market(s)

health conscious group

Requirements
Must have
• modern feel, honey and apple picture

```html
<!DOCTYPE html>
<html lang="en">
<head>
<meta charset="utf-8">
<title>Velora Apple Cider Vinegar with Honey – Label</title>
<link href="https://fonts.googleapis.com/css2?family=Pathway+Gothic+One&family=Dancing+Script:wght@500&family=Montserrat:wght@400;600;700&display=swap" rel="stylesheet">
<style>
  :root{
    --bg:#ececec;
    --paper:#ffffff;
    --red:#c8203a;
    --orange:#f39a1e;
    --ink:#3a2f4a;
    --text:#2b2b2b;
    --green:#6aa82a;
    --badge:#7db43a;
  }
  *{box-sizing:border-box;margin:0;padding:0}
  html,body{width:1200px;height:1200px;overflow:hidden;background:var(--bg)}
  body{font-family:"Montserrat",sans-serif;position:relative}
  .label{
    position:absolute;left:315px;top:110px;width:570px;height:980px;
    background:var(--paper);
    border-top-left-radius:285px 230px;border-top-right-radius:285px 230px;
    box-shadow:0 10px 30px rgba(0,0,0,.12);
    overflow:hidden;
  }
  .brand{position:absolute;top:95px;left:0;width:100%;display:flex;flex-direction:column;align-items:center;gap:16px}
  .brand-dot{width:62px;height:62px;border-radius:50%;background:var(--orange)}
  .brand-name{font-weight:700;font-size:50px;color:var(--ink);letter-spacing:1px;line-height:1}
  .title{position:absolute;left:28px;top:290px;font-family:"Pathway Gothic One",sans-serif;font-weight:400;line-height:.86;text-transform:uppercase}
  .title .line{display:block}
  .title .apple,.title .vinegar{font-size:140px;color:var(--red)}
  .title .honey{font-size:118px;color:var(--orange);letter-spacing:2px}
  .title .with{position:absolute;left:170px;top:222px;font-family:"Dancing Script",cursive;font-size:34px;color:var(--orange);text-transform:none}
  .honey-dipper{position:absolute;left:410px;top:460px;width:170px;height:190px;border-radius:90px 0 0 90px;
    background:linear-gradient(160deg,#f4b64a 0%,#e79a22 55%,#c97a12 100%)}
  .apple-photo{position:absolute;left:330px;top:700px;width:280px;height:280px;border-radius:50%;
    background:radial-gradient(circle at 40% 35%,#ea3a48 0%,#cf1c2e 45%,#a30f1d 100%)}
  .usage{position:absolute;left:28px;top:672px;font-size:24px;color:var(--text)}
  .steps{position:absolute;left:0;top:712px;width:335px;padding:12px 30px 12px 28px;background:var(--red);color:#fff;font-size:15px;line-height:1.3;
    clip-path:polygon(0 0,100% 0,92% 100%,0 100%)}
  .steps li{list-style:none;padding-left:14px;position:relative}
  .steps li::before{content:"";position:absolute;left:0;top:6px;width:6px;height:6px;border:1px solid #fff;border-radius:50%}
  .ingredients{position:absolute;left:28px;top:826px;width:290px;font-size:11.5px;font-weight:700;line-height:1.3;color:var(--text)}
  .storage{position:absolute;left:28px;top:882px;font-size:8.5px;font-weight:700;color:var(--text)}
  .badges{position:absolute;left:28px;top:908px;display:flex;gap:12px}
  .badge{width:46px;height:46px;border-radius:50%;background:var(--badge);border:3px solid #fff;box-shadow:0 0 0 2px var(--badge)}
  .best{position:absolute;left:215px;top:912px;font-size:9px;font-weight:700;color:var(--text)}
  .volume{position:absolute;right:30px;top:920px;font-weight:700;font-size:30px;color:var(--green)}
</style>
</head>
<body>
  <div class="label">
    <div class="brand">
      <span class="brand-dot"></span>
      <span class="brand-name">Velora</span>
    </div>
    <div class="honey-dipper" role="img" aria-label="Honey dripping from a wooden dipper"></div>
    <div class="apple-photo" role="img" aria-label="Fresh red apple catching the honey drip"></div>
    <h1 class="title">
      <span class="line apple">Apple Cider</span>
      <span class="line vinegar">Vinegar</span>
      <span class="with">with</span>
      <span class="line honey">Honey</span>
    </h1>
    <p class="usage">instruction for use:</p>
    <ul class="steps">
      <li>add 20ml to a full glass of water</li>
      <li>3 times a days before meal</li>
      <li>stop consuming if allergies happen</li>
    </ul>
    <p class="ingredients">INGREDIENT:<br>HONEY, APPLE CIDER VINEGAR, WATER,<br>NO ARTIFICIAL COLOR &amp; PRESERVATIVE</p>
    <p class="storage">STORE IN COOL PLACE, DO NOT EXPOSE TO SUNLIGHT</p>
    <div class="badges">
      <span class="badge"></span><span class="badge"></span><span class="badge"></span>
    </div>
    <p class="best">BEST BEFORE:</p>
    <p class="volume">400 ml</p>
  </div>
</body>
</html>
```